Business card / stationery design
Pemberton Hale Warrick
Project: Business card / stationery design
Business card / stationery design - Engineering
Creative Brief
Use specific fonts
Gill Sans MT, Calibri, Corbel, Lucida Sans UC or similar
Professional
Derek R. Pemberton, P.E., LEED A.P., CPMP
Principal
4738 E. Harrowgate Ave., Suite C-212B, Springfield, Missouri 65809
dpemberton@pembertonhalewarrick.example
www.pembertonhalewarrick.example
We would like to use only the logo from the attached file. We like the current color arrangement, but would be interested in seeing it in other colors. Also the slightly gray color behind the logo should just be white or whatever the background color is. A couple of examples are attached. The main text adjacent to the logo should read: Pemberton Hale Warrick. Secondary text will be similar to: Engineering & Energy Services.
We are interested in your ideas.

```html
<!DOCTYPE html>
<html lang="en">
<head>
<meta charset="utf-8">
<title>Pemberton Hale Warrick — Stationery</title>
<link href="https://fonts.googleapis.com/css2?family=Cabin:wght@400;600&display=swap" rel="stylesheet">
<style>
:root{
  --bg:#e9e7e4;
  --paper:#ffffff;
  --ink:#3a3a3a;
  --muted:#777777;
  --green:#7ab23a;
  --green-dark:#4f8a24;
  --blue:#2a86c8;
  --blue-dark:#13598f;
  --black:#1c1c1c;
  --shadow:0 2px 6px rgba(0,0,0,.18);
}
*{box-sizing:border-box;margin:0;padding:0}
html,body{width:1200px;height:497px;overflow:hidden}
body{background:var(--bg);font-family:"Cabin",Calibri,sans-serif;color:var(--ink);position:relative}
.card,.letterhead,.envelope{position:absolute;box-shadow:var(--shadow)}
.card{width:180px;height:120px;border-radius:6px;background:var(--paper);overflow:hidden}
.card--blue{background:linear-gradient(135deg,var(--blue),var(--blue-dark))}
.card--green{background:linear-gradient(135deg,var(--green),var(--green-dark))}
.card--black{background:var(--black)}
.brand{display:flex;align-items:center;gap:5px}
.brand-mark{width:12px;height:12px;background:var(--green);flex:none}
.brand-name{font-size:8.5px;font-weight:600;letter-spacing:.06em;text-transform:uppercase;color:var(--ink);white-space:nowrap}
.tagline{font-size:5px;letter-spacing:.1em;text-transform:uppercase;color:var(--muted);margin-top:2px}
.card--blue .brand-name,.card--green .brand-name,.card--black .brand-name,
.card--blue .tagline,.card--green .tagline,.card--black .tagline{color:#fff}
.card--blue .brand-mark,.card--green .brand-mark,.card--black .brand-mark{background:#fff}
.card-center{position:absolute;left:22px;top:48px}
.card-contact{position:absolute;left:16px;top:14px;right:8px}
.card-contact .brand{position:absolute;left:0;top:68px}
.contact{margin-left:56px;font-size:4.5px;line-height:1.45;color:var(--ink);white-space:nowrap}
.contact .person{font-size:5.6px;font-weight:600;color:var(--blue-dark)}
.letterhead{left:412px;top:34px;width:240px;height:440px;background:var(--paper)}
.letterhead .brand{position:absolute;left:20px;top:22px;gap:4px}
.letterhead .brand-mark{width:10px;height:10px}
.letterhead .brand-name{font-size:6.5px}
.letterhead .contact{position:absolute;left:158px;top:18px;margin:0;font-size:4.2px}
.envelope{background:var(--paper);overflow:hidden}
.envelope svg{position:absolute;left:0;top:0}
.env-back{left:744px;top:28px;width:446px;height:236px}
.env-middle{left:720px;top:106px;width:470px;height:230px}
.env-front{left:660px;top:204px;width:468px;height:276px}
.env-front .brand{position:absolute;left:202px;top:54px}
.env-front .brand-name{color:#fff}
.env-front .brand-mark{background:#fff}
.env-front .return{position:absolute;left:26px;top:196px;font-size:4.8px;line-height:1.5;color:var(--ink)}
</style>
</head>
<body>

<section class="card" style="left:24px;top:50px">
  <div class="card-contact">
    <div class="contact">
      <div class="person">Derek R. Pemberton, P.E.</div>
      <div>Principal</div><br>
      <div>4738 E. Harrowgate Ave., Suite C-212B</div>
      <div>Springfield, Missouri 65809</div>
      <div>Phone: 417.555.0142</div>
      <div>dpemberton@pembertonhalewarrick.example</div>
    </div>
    <div class="brand"><span class="brand-mark"></span><span class="brand-name">Pemberton Hale Warrick</span></div>
  </div>
</section>
<section class="card" style="left:220px;top:50px">
  <div class="card-contact">
    <div class="contact">
      <div class="person">Derek R. Pemberton, P.E.</div>
      <div>Principal</div><br>
      <div>4738 E. Harrowgate Ave., Suite C-212B</div>
      <div>Springfield, Missouri 65809</div>
      <div>Fax: 417.555.0143</div>
      <div>www.pembertonhalewarrick.example</div>
    </div>
    <div class="brand"><span class="brand-mark"></span><span class="brand-name">Pemberton Hale Warrick</span></div>
  </div>
</section>
<section class="card card--blue" style="left:24px;top:188px">
  <div class="card-center"><div class="brand"><span class="brand-mark"></span><span class="brand-name">Pemberton Hale Warrick</span></div><div class="tagline">Engineering &amp; Energy Services</div></div>
</section>
<section class="card card--green" style="left:220px;top:188px">
  <div class="card-center"><div class="brand"><span class="brand-mark"></span><span class="brand-name">Pemberton Hale Warrick</span></div><div class="tagline">Engineering &amp; Energy Services</div></div>
</section>
<section class="card" style="left:24px;top:326px">
  <div class="card-center"><div class="brand"><span class="brand-mark"></span><span class="brand-name">Pemberton Hale Warrick</span></div><div class="tagline">Engineering &amp; Energy Services</div></div>
</section>
<section class="card card--black" style="left:220px;top:326px">
  <div class="card-center"><div class="brand"><span class="brand-mark"></span><span class="brand-name">Pemberton Hale Warrick</span></div><div class="tagline">Engineering &amp; Energy Services</div></div>
</section>

<section class="letterhead">
  <div class="brand"><span class="brand-mark"></span><span class="brand-name">Pemberton Hale Warrick</span></div>
  <div class="contact">
    <div>4738 E. Harrowgate Ave.</div>
    <div>Suite C-212B</div>
    <div>Springfield, Missouri 65809</div>
    <div>Phone: 417.555.0142</div>
    <div>www.pembertonhalewarrick.example</div>
  </div>
</section>

<section class="envelope env-back">
  <svg width="446" height="236" viewBox="0 0 446 236">
    <defs><linearGradient id="gFlap" x1="0" y1="0" x2="0" y2="1"><stop offset="0" stop-color="#4f8a24"/><stop offset="1" stop-color="#7ab23a"/></linearGradient></defs>
    <path d="M0 0H446L223 120Z" fill="url(#gFlap)"/>
  </svg>
</section>
<section class="envelope env-middle">
  <svg width="470" height="230" viewBox="0 0 470 230">
    <path d="M0 0L235 118L470 0" fill="none" stroke="#d4d4d4" stroke-width="1.5"/>
  </svg>
</section>
<section class="envelope env-front">
  <svg width="468" height="276" viewBox="0 0 468 276">
    <defs><linearGradient id="bFlap" x1="0" y1="0" x2="0" y2="1"><stop offset="0" stop-color="#13598f"/><stop offset="1" stop-color="#2a86c8"/></linearGradient></defs>
    <path d="M0 0H468L234 130Z" fill="url(#bFlap)"/>
  </svg>
  <div class="brand"><span class="brand-mark"></span><span class="brand-name">Pemberton Hale Warrick</span></div>
  <div class="return">
    <div>4738 E. Harrowgate Ave.</div>
    <div>Suite C-212B</div>
    <div>Springfield, Missouri 65809</div>
    <div>Phone: 417.555.0142</div>
    <div>www.pembertonhalewarrick.example</div>
  </div>
</section>

</body>
</html>
```